Fun and Splashy Flyer Design

We need a flyer designed for our new car cleaning brand! We have looked around, and the stock options either look way too dark/serious/exclusive, or they look too shiny/stock image.

We need something that can be more subtle, that works with our work van.

For this project we would like a photoshop file with individual layers, and you can just put placeholder text for the main slogan, a header 1, header 2, bullet point and body text.

What we're really looking for are the transitions between images and elements, font colours and pairings and design accents.

We want the brand to be fun, clean, happy and straightforward (slightly minimalist). Please message if you have any questions!

```html
<!DOCTYPE html>
<html lang="en">
<head>
<meta charset="utf-8">
<title>Mobile Car Cleaning and Detailing Flyer</title>
<link rel="stylesheet" href="https://fonts.googleapis.com/css2?family=Roboto:ital,wght@1,700;1,900&family=Montserrat:ital,wght@0,400;0,500;0,700;0,800;1,300&display=swap">
<style>
  :root {
    --blue: #0a77c2;
    --blue-deep: #0563a8;
    --blue-light: #3d9fdc;
    --yellow: #f7cc0c;
    --yellow-deep: #e8b900;
    --white: #ffffff;
    --ink: #1d1d1f;
    --red: #c0141c;
  }
  * { margin: 0; padding: 0; box-sizing: border-box; }
  html, body { width: 703px; height: 1200px; overflow: hidden; background: #ffffff; }
  .flyer {
    position: relative; width: 703px; height: 1200px; overflow: hidden;
    background: linear-gradient(180deg, var(--blue) 0%, #1383cc 30%, #2b93d6 40%, #8fc6ea 48%, #ffffff 58%, #ffffff 100%);
    font-family: "Montserrat", sans-serif; color: var(--ink);
  }
  .accents { position: absolute; left: 0; top: 0; }
  .headline { position: absolute; left: 0; right: 0; top: 36px; text-align: center;
    font-family: "Roboto", sans-serif; font-style: italic; font-weight: 900; line-height: 1; }
  .headline .line-mobile { display: block; color: var(--white); font-size: 60px; letter-spacing: 0.5px; }
  .headline .line-cleaning { display: block; color: var(--yellow); font-size: 76px; margin-top: 2px; }
  .headline .line-detailing { display: flex; justify-content: center; align-items: center; gap: 10px;
    color: var(--white); font-size: 48px; margin-top: 4px; }
  .dash-rule { display: inline-block; width: 64px; height: 9px;
    background: repeating-linear-gradient(180deg, var(--yellow) 0 2px, transparent 2px 4px); }
  .slogan { position: absolute; left: 0; right: 0; top: 236px; text-align: center;
    font-family: "Montserrat", sans-serif; font-style: italic; font-weight: 300; font-size: 31px; color: var(--white); }
  .taglines { position: absolute; top: 296px; left: 74px; right: 74px; display: flex; justify-content: space-between;
    font-family: "Roboto", sans-serif; font-style: italic; font-weight: 700; font-size: 15.5px; color: var(--white); }
  .hero-photo { position: absolute; left: 0; top: 330px; width: 703px; height: 380px;
    background: radial-gradient(ellipse 46% 36% at 52% 52%, #c5161e 0%, #a8121a 45%, rgba(210,225,238,0.7) 78%, rgba(255,255,255,0) 100%); }
  .section-title { position: absolute; left: 47px; font-family: "Montserrat", sans-serif; font-weight: 800;
    color: var(--blue); letter-spacing: 0.3px; }
  .section-title::after { content: ""; position: absolute; left: 0; bottom: -12px; width: 54px; height: 4px; background: var(--yellow); }
  .services-title { top: 712px; font-size: 27px; }
  .detail-title { top: 932px; font-size: 28px; }
  .service-list { position: absolute; left: 47px; top: 774px; list-style: none; }
  .service-list li { display: flex; align-items: center; gap: 14px; height: 38.5px; font-size: 14px; font-weight: 500; }
  .tick { width: 16px; height: 16px; flex: none; }
  .service-photo { position: absolute; top: 760px; width: 128px; height: 128px; border-radius: 50%;
    border: 3px solid var(--yellow); box-shadow: 0 0 0 2px var(--blue); }
  .wheel { left: 281px; background: radial-gradient(circle at 45% 50%, #c9ccd1 0%, #5b6068 55%, #23262b 100%); }
  .polish { left: 414px; background: linear-gradient(160deg, #3a3f47 0%, #1c1f24 55%, #8d939b 100%); }
  .engine { left: 548px; background: radial-gradient(circle at 50% 50%, #9a6a4d 0%, #4c3429 55%, #20191a 100%); }
  .body-copy { position: absolute; left: 47px; top: 1006px; width: 432px; font-size: 12.6px; line-height: 17.4px;
    text-align: justify; color: var(--ink); }
  .brand-seal { position: absolute; left: 521px; top: 1017px; width: 132px; height: 132px; border-radius: 50%;
    background: var(--blue-light); border: 5px solid var(--yellow); box-shadow: 0 0 0 3px var(--blue);
    display: flex; align-items: center; justify-content: center; text-align: center; }
  .brand-name { font-family: "Montserrat", sans-serif; font-weight: 800; font-size: 17px; line-height: 1.15; color: var(--white); }
  .footer-band { position: absolute; left: 0; top: 1110px; }
  .contact { position: absolute; left: 47px; top: 1130px; }
  .call { font-size: 20px; font-weight: 500; color: var(--ink); letter-spacing: 0.3px; }
  .call strong { font-size: 25px; font-weight: 700; }
  .web { font-size: 17px; font-weight: 500; color: var(--ink); margin-top: 1px; }
  .social-mark { position: absolute; left: 372px; top: 1158px; width: 15px; height: 15px; background: var(--blue); }
</style>
</head>
<body>
<div class="flyer">

  <svg class="accents" width="703" height="1200" viewBox="0 0 703 1200" aria-hidden="true">
    <path d="M0 430 C20 400 40 385 70 370 C40 400 20 440 0 520 Z" fill="var(--yellow)"/>
    <path d="M640 500 C665 480 690 478 703 480 L703 520 C690 505 665 500 640 500 Z" fill="var(--yellow)"/>
  </svg>

  <h1 class="headline">
    <span class="line-mobile">MOBILE</span>
    <span class="line-cleaning">CAR CLEANING</span>
    <span class="line-detailing"><span class="dash-rule"></span>AND DETAILING<span class="dash-rule"></span></span>
  </h1>

  <p class="slogan">Best Car Cleaning in Town</p>
  <div class="taglines"><span>Professional Car Wash</span><span>We Make Your Car Absolutely Clean</span></div>

  <div class="hero-photo" role="img" aria-label="Photo of a glossy red sports car splashed with water while a worker washes it with a pressure hose"></div>

  <h2 class="section-title services-title">OUR SERVICES</h2>
  <ul class="service-list">
    <li><svg class="tick" viewBox="0 0 16 16"><rect x="1" y="3" width="12" height="12" fill="none" stroke="var(--yellow-deep)" stroke-width="1.6"/><path d="M4 8 L7 11 L15 2" fill="none" stroke="var(--yellow-deep)" stroke-width="1.8"/></svg>Wax &amp; Shine</li>
    <li><svg class="tick" viewBox="0 0 16 16"><rect x="1" y="3" width="12" height="12" fill="none" stroke="var(--yellow-deep)" stroke-width="1.6"/><path d="M4 8 L7 11 L15 2" fill="none" stroke="var(--yellow-deep)" stroke-width="1.8"/></svg>Scratch Removal</li>
    <li><svg class="tick" viewBox="0 0 16 16"><rect x="1" y="3" width="12" height="12" fill="none" stroke="var(--yellow-deep)" stroke-width="1.6"/><path d="M4 8 L7 11 L15 2" fill="none" stroke="var(--yellow-deep)" stroke-width="1.8"/></svg>Water Spot Removal</li>
    <li><svg class="tick" viewBox="0 0 16 16"><rect x="1" y="3" width="12" height="12" fill="none" stroke="var(--yellow-deep)" stroke-width="1.6"/><path d="M4 8 L7 11 L15 2" fill="none" stroke="var(--yellow-deep)" stroke-width="1.8"/></svg>Paint Restoration</li>
  </ul>

  <div class="service-photo wheel" role="img" aria-label="Photo of a hand wiping a car wheel rim with a cloth"></div>
  <div class="service-photo polish" role="img" aria-label="Photo of a polishing machine buffing a dark car bonnet"></div>
  <div class="service-photo engine" role="img" aria-label="Photo of hands cleaning an engine bay with a cloth"></div>

  <h2 class="section-title detail-title">DETAILED CAR CLEANING</h2>
  <p class="body-copy">Lorem Ipsum is simply dummy text of the printing and typesetting industry. Lorem Ipsum has been the industry's standard dummy text ever since the 1500s, when an unknown printer took a galley of type and scrambled it to make a type specimen book. It has survived not only five centuries, but also the leap into electronic typesetting, remaining essentially unchanged.</p>

  <div class="brand-seal"><span class="brand-name">Bright<br>Wash<br>Crew</span></div>

  <svg class="footer-band" width="703" height="90" viewBox="0 0 703 90" aria-hidden="true">
    <path d="M0 0 L330 0 C400 0 440 40 470 82 L0 82 Z" fill="var(--yellow)"/>
    <rect x="0" y="82" width="703" height="8" fill="var(--yellow)"/>
    <rect x="462" y="77" width="241" height="5" fill="var(--blue)"/>
  </svg>

  <div class="contact">
    <p class="call">CALL US NOW: <strong>0198765432</strong></p>
    <p class="web">www.brightwashcrew.ca</p>
  </div>
  <span class="social-mark" aria-hidden="true"></span>

</div>
</body>
</html>
```